Web app UI design

This web app has been built and the UI needs a refresh.

Attached are the pages which need the refresh.

The web app is for a cyber security product/service and customers are inputting their details.

```html
<!DOCTYPE html>
<html lang="en">
<head>
<meta charset="UTF-8">
<title>Certiva – Available Packages</title>
<link rel="stylesheet" href="https://fonts.googleapis.com/css2?family=Roboto:wght@400;500&family=Roboto+Condensed:wght@400;500;700&display=swap">
<style>
  :root{
    --sidebar:#2e3346;
    --sidebar-top:#232838;
    --sidebar-active:#252a3b;
    --sidebar-text:#ffffff;
    --sidebar-muted:#9aa0ad;
    --accent:#3d8ef0;
    --accent-soft:#b9d7fb;
    --page:#f0f2f6;
    --white:#ffffff;
    --ink:#1f2230;
    --muted:#9a9a9a;
    --tick-bg:#dcf5dc;
    --tick:#4cc24c;
    --bronze:#cf7c3a;
    --silver:#c3c7cc;
    --gold:#ffe100;
    --online:#2ecc40;
  }
  *{box-sizing:border-box;margin:0;padding:0}
  html,body{width:1200px;height:818px;overflow:hidden}
  body{position:relative;background:var(--page);font-family:'Roboto',sans-serif;color:var(--ink)}

  .sidebar{position:absolute;left:0;top:0;width:217px;height:818px;background:var(--sidebar)}
  .brand{height:70px;background:var(--sidebar-top);display:flex;align-items:center;padding-left:44px;gap:12px;color:var(--white)}
  .brand-mark{width:20px;height:20px;border-radius:50%;background:var(--white)}
  .brand-name{font-size:16px;letter-spacing:6px;font-weight:400}
  .nav{position:absolute;top:123px;left:0;width:100%;list-style:none}
  .nav-item{height:42px;display:flex;align-items:center;padding-left:28px;gap:14px;color:var(--sidebar-text);font-size:13.5px;position:relative}
  .nav-item svg{width:18px;height:18px;fill:#e7e9ee}
  .nav-item.active{background:var(--sidebar-active)}
  .nav-item.active::before{content:"";position:absolute;left:0;top:0;width:7px;height:100%;background:var(--accent)}
  .logout{position:absolute;top:762px;left:0;width:100%;display:flex;justify-content:center;align-items:center;gap:7px;color:var(--sidebar-muted);font-size:13px}
  .logout svg{width:14px;height:14px;fill:var(--sidebar-muted)}
  .legal{position:absolute;top:793px;left:0;width:100%;text-align:center;color:var(--sidebar-muted);font-size:9.5px}

  .topbar{position:absolute;left:217px;top:0;right:0;height:75px;background:var(--white);border-bottom:7px solid #eceef2}
  .menu-btn{position:absolute;left:26px;top:17px;width:40px;height:40px;border-radius:50%;background:#eff0f3;display:flex;align-items:center;justify-content:center}
  .user{position:absolute;right:37px;top:10px;display:flex;align-items:center;gap:12px}
  .user-info{text-align:right}
  .user-name{font-size:15px;color:#111}
  .user-status{font-size:9.5px;color:#777;margin-top:2px}
  .avatar{width:54px;height:54px;border-radius:50%;background:linear-gradient(135deg,#8fb6d6,#4b4a4a 55%,#c9a27a);position:relative}
  .avatar::after{content:"";position:absolute;left:0;bottom:2px;width:11px;height:11px;border-radius:50%;background:var(--online)}
  .chevron{width:14px;height:14px;margin-left:4px}

  .page-head{position:absolute;left:217px;top:82px;right:0;height:100px;background:var(--white)}
  .page-title{position:absolute;left:41px;top:29px;height:41px;border-left:8px solid var(--ink);padding-left:15px;display:flex;align-items:center;font-family:'Roboto Condensed',sans-serif;font-size:24px;font-weight:400}
  .help{position:absolute;right:43px;top:39px;display:flex;align-items:center;gap:6px;color:var(--accent);font-family:'Roboto Condensed',sans-serif;font-size:15px}

  .plan{position:absolute;top:232px;width:283px;height:416px;background:var(--white);border-radius:4px;border-top:7px solid;text-align:center}
  .plan.bronze{left:267px;border-top-color:var(--bronze)}
  .plan.silver{left:567px;border-top-color:var(--silver)}
  .plan.gold{left:867px;border-top-color:var(--gold)}
  .plan-icon{position:absolute;left:50%;top:34px;margin-left:-9px;width:18px;height:22px;fill:var(--ink)}
  .plan-name{position:absolute;left:0;right:0;top:58px;font-family:'Roboto Condensed',sans-serif;font-size:30px;font-weight:500;color:#222}
  .perks{position:absolute;left:27px;right:18px;top:116px;list-style:none;display:flex;flex-direction:column;gap:12px;text-align:left}
  .perk{display:flex;align-items:center;gap:9px;font-size:13.3px;line-height:16px;color:var(--muted)}
  .tick{flex:0 0 18px;height:18px;border-radius:50%;background:var(--tick-bg);display:flex;align-items:center;justify-content:center}
  .price{position:absolute;left:0;right:0;font-family:'Roboto Condensed',sans-serif;color:#222}
  .price.amount{top:250px;font-size:42px}
  .price.quote{top:270px;font-size:23px}
  .price sup{font-size:14px;vertical-align:top;position:relative;top:4px}
  .price.amount sup{font-size:18px;top:2px}
  .period{position:absolute;left:0;right:0;top:309px;font-family:'Roboto Condensed',sans-serif;font-size:15.5px;color:#333;letter-spacing:.3px}
  .plan-btn{position:absolute;left:20px;right:20px;top:351px;height:42px;border-radius:2px;background:var(--accent);color:var(--white);font-size:13.5px;font-weight:500;display:flex;align-items:center;justify-content:center;gap:8px}
  .plan-btn.subscribed{background:var(--accent-soft)}
  .plan-btn .done{width:17px;height:17px;border-radius:50%;background:rgba(255,255,255,.45);display:flex;align-items:center;justify-content:center}

  .manage{position:absolute;left:972px;top:705px;width:178px;height:50px;background:var(--accent);color:var(--white);border-radius:2px;display:flex;align-items:center;justify-content:center;font-size:13.5px;font-weight:500}
  .copyright{position:absolute;left:258px;top:793px;font-size:9.5px;color:#444}
</style>
</head>
<body>
  <aside class="sidebar">
    <div class="brand"><span class="brand-mark"></span><span class="brand-name">CERTIVA</span></div>
    <ul class="nav">
      <li class="nav-item"><svg viewBox="0 0 20 20"><path d="M10 2 2 9v9h6v-6h4v6h6V9z"/></svg>Home</li>
      <li class="nav-item active"><svg viewBox="0 0 20 20"><path d="M1 3h3l1 3h13l-2 7H6.5L4 5.2 3 5H1z"/><circle cx="8" cy="17" r="1.6"/><circle cx="15" cy="17" r="1.6"/></svg>Subscriptions</li>
      <li class="nav-item"><svg viewBox="0 0 20 20"><path d="M5 9V6a5 5 0 0 1 10 0v3h1v10H4V9zm2 0h6V6a3 3 0 0 0-6 0z"/></svg>Verify</li>
      <li class="nav-item"><svg viewBox="0 0 20 20"><path d="M10 1l8 4.5v9L10 19l-8-4.5v-9zm0 6.5a2.5 2.5 0 1 0 0 5 2.5 2.5 0 0 0 0-5z"/></svg>Settings</li>
    </ul>
    <div class="logout"><svg viewBox="0 0 16 16"><path d="M1 1h14v14H1zm4 6v2h4v2l3-3-3-3v2z"/></svg>Log out</div>
    <div class="legal">Privacy policy &nbsp;|&nbsp; Contact us</div>
  </aside>

  <header class="topbar">
    <div class="menu-btn"><svg width="16" height="14" viewBox="0 0 16 14"><path d="M0 1h16M0 7h16M0 13h16" stroke="#1f2230" stroke-width="1.8"/></svg></div>
    <div class="user">
      <div class="user-info"><div class="user-name">User’s Name</div><div class="user-status">Online</div></div>
      <div class="avatar" role="img" aria-label="User profile photo"></div>
      <svg class="chevron" viewBox="0 0 14 14"><path d="M2 5l5 5 5-5" fill="none" stroke="#333" stroke-width="1.6"/></svg>
    </div>
  </header>

  <section class="page-head">
    <h1 class="page-title">Available Packages</h1>
    <div class="help">Need help
      <svg width="17" height="17" viewBox="0 0 18 18"><circle cx="9" cy="9" r="8" fill="none" stroke="#3d8ef0" stroke-width="1.6"/><path d="M6.8 7a2.2 2.2 0 1 1 3.2 2c-.7.4-1 .8-1 1.6" fill="none" stroke="#3d8ef0" stroke-width="1.6"/><circle cx="9" cy="13.2" r="1" fill="#3d8ef0"/></svg>
    </div>
  </section>

  <svg width="0" height="0" style="position:absolute">
    <defs>
      <symbol id="rocket" viewBox="0 0 18 22"><path d="M9 0c3 2.5 4.5 6 4.5 10v5l2.5 2v2h-4l-1 1H7l-1-1H2v-2l2.5-2v-5C4.5 6 6 2.5 9 0zm0 7a1.8 1.8 0 1 0 0 3.6A1.8 1.8 0 0 0 9 7zM7.5 20.5h3L9 22z"/></symbol>
      <symbol id="check" viewBox="0 0 10 10"><path d="M1.5 5.2 4 7.5 8.5 2.8" fill="none" stroke="#4cc24c" stroke-width="1.4"/></symbol>
    </defs>
  </svg>

  <article class="plan bronze">
    <svg class="plan-icon"><use href="#rocket"/></svg>
    <h2 class="plan-name">Bronze</h2>
    <ul class="perks">
      <li class="perk"><span class="tick"><svg width="10" height="10"><use href="#check"/></svg></span>Access to verification system</li>
      <li class="perk"><span class="tick"><svg width="10" height="10"><use href="#check"/></svg></span>Use of certiva logo and material on website and document</li>
      <li class="perk"><span class="tick"><svg width="10" height="10"><use href="#check"/></svg></span>Other perks...</li>
    </ul>
    <div class="price amount"><sup>$</sup>85/</div>
    <div class="period">per month</div>
    <div class="plan-btn subscribed"><span class="done"><svg width="10" height="10" viewBox="0 0 10 10"><path d="M1.5 5.2 4 7.5 8.5 2.8" fill="none" stroke="#fff" stroke-width="1.5"/></svg></span>Subscribed</div>
  </article>

  <article class="plan silver">
    <svg class="plan-icon"><use href="#rocket"/></svg>
    <h2 class="plan-name">Silver</h2>
    <ul class="perks">
      <li class="perk"><span class="tick"><svg width="10" height="10"><use href="#check"/></svg></span>Access to verification system</li>
      <li class="perk"><span class="tick"><svg width="10" height="10"><use href="#check"/></svg></span>Use of certiva logo and material on website and document</li>
      <li class="perk"><span class="tick"><svg width="10" height="10"><use href="#check"/></svg></span>Other perks...</li>
    </ul>
    <div class="price quote"><sup>$</sup>Contact us for price/</div>
    <div class="period">per month</div>
    <div class="plan-btn">Subscribe Now</div>
  </article>

  <article class="plan gold">
    <svg class="plan-icon"><use href="#rocket"/></svg>
    <h2 class="plan-name">Gold</h2>
    <ul class="perks">
      <li class="perk"><span class="tick"><svg width="10" height="10"><use href="#check"/></svg></span>Access to verification system</li>
      <li class="perk"><span class="tick"><svg width="10" height="10"><use href="#check"/></svg></span>Use of certiva logo and material on website and document</li>
      <li class="perk"><span class="tick"><svg width="10" height="10"><use href="#check"/></svg></span>Access to verification system</li>
      <li class="perk"><span class="tick"><svg width="10" height="10"><use href="#check"/></svg></span>Other perks...</li>
    </ul>
    <div class="price quote"><sup>$</sup>Contact us for price/</div>
    <div class="period">per month</div>
    <div class="plan-btn">Subscribe Now</div>
  </article>

  <div class="manage">Manage Subscription</div>
  <footer class="copyright">Certiva @ 2023</footer>
</body>
</html>
```